Veltrisk inc. Aviation website

we are looking for a very modern and luxury web design, we are an aviation based company and specialize in aircraft exports and setup of air services world wide.
we want the website to be unique, creative, luxurious, professional, and to make an statement.
we have attached the logo.
our business cards theme is black background with gold stamping, if that is the rout you want to take.
**The format we are looking for is Wordpress.**
**the website is www.veltriskinc-example.com**
** 3 pages:
1. home page: -overview/about us
-industry leading
- worldwide presence
- aerial support
2. products and services: -business aircrafts
-commercial aircrafts
-amphibious aircrafts
-operation setup
-maintenance & crew training
3. contact us
**our location: Marlow Fenwick Harbour Airfield, Hangar 6**
we do appreciate suggestions
Thank you all.
Target Market(s)
Aviation professionals, Aircraft import/export, airlines, air taxi operations
Industry/Entity Type
It Company
Number of Pages Required
3 page
Requirements
Must have
- must have a very modern and luxurious design, and must be aviation oriented, and must have the logo, must be professional looking and be animated.
Nice to have
- black, gold, and burgandy colour
Should not have
- should not be playful and cartoony.

```html
<!DOCTYPE html>
<html lang="en">
<head>
<meta charset="utf-8">
<title>Veltrisk inc. — Services</title>
<link rel="stylesheet" href="https://fonts.googleapis.com/css2?family=Dosis:wght@500&family=Lato:wght@400;700&display=swap">
<style>
  :root {
    --gold: #d9a12a;
    --gold-text: #c8922c;
    --header-bg: #151513;
    --white: #ffffff;
    --ink: #111111;
    --cutout: #2e2419;
    --sky-top: #2a2a28;
    --sky-mid: #4a3a2a;
    --horizon: #6e4a26;
    --ground: #1a1714;
  }
  html, body {
    margin: 0;
    padding: 0;
    width: 1200px;
    height: 699px;
    overflow: hidden;
    background: var(--white);
  }
  .page {
    position: relative;
    width: 1200px;
    height: 699px;
    font-family: "Lato", Arial, sans-serif;
  }
  .site-header {
    position: absolute;
    top: 0; left: 0;
    width: 1200px;
    height: 58px;
    background: var(--header-bg);
    border-bottom: 1px solid #2a2a28;
    z-index: 2;
  }
  .brand {
    position: absolute;
    left: 129px;
    top: 14px;
    font-family: "Dosis", Arial, sans-serif;
    font-weight: 500;
    font-size: 27px;
    letter-spacing: 2px;
    color: var(--gold);
    text-transform: uppercase;
    line-height: 1;
  }
  .main-nav {
    position: absolute;
    right: 129px;
    top: 22px;
    display: flex;
    gap: 27px;
    font-family: "Dosis", Arial, sans-serif;
    font-weight: 500;
    font-size: 13px;
    color: var(--white);
    text-transform: uppercase;
    letter-spacing: 0.2px;
  }
  .main-nav a { color: inherit; text-decoration: none; }
  .hero {
    position: absolute;
    top: 58px; left: 0;
    width: 1200px;
    height: 595px;
    background:
      radial-gradient(ellipse 420px 160px at 320px 330px, rgba(140,85,35,0.55), rgba(0,0,0,0) 70%),
      radial-gradient(ellipse 500px 260px at 900px 250px, rgba(70,70,70,0.35), rgba(0,0,0,0) 70%),
      linear-gradient(180deg, var(--sky-top) 0%, var(--sky-mid) 40%, var(--horizon) 56%, #2e2419 68%, var(--ground) 100%);
  }
  .service {
    position: absolute;
    width: 240px;
    margin-left: -120px;
    text-align: center;
  }
  .service svg { display: block; margin: 0 auto; }
  .service-title {
    margin: 0;
    font-weight: 700;
    font-size: 22px;
    line-height: 25px;
    color: var(--white);
    text-transform: uppercase;
  }
  .site-footer {
    position: absolute;
    left: 0; top: 653px;
    width: 1200px;
    height: 46px;
    background: var(--white);
  }
  .copyright {
    position: absolute;
    left: 129px;
    top: 15px;
    margin: 0;
    font-size: 13px;
    color: var(--gold-text);
  }
  .social {
    position: absolute;
    right: 129px;
    top: 16px;
    display: flex;
    gap: 8px;
  }
  .social span {
    width: 17px; height: 17px;
    border-radius: 50%;
    background: var(--ink);
  }
</style>
</head>
<body>
<div class="page">
  <header class="site-header">
    <div class="brand">Veltrisk inc.</div>
    <nav class="main-nav">
      <a href="#">Home</a>
      <a href="#">Services</a>
      <a href="#">Contact Us</a>
    </nav>
  </header>

  <main class="hero" role="img" aria-label="Business jet parked on a wet runway at sunset">
    <div class="service service-business" style="left:380px; top:101px;">
      <svg width="112" height="78" viewBox="0 0 112 80" fill="var(--gold)">
        <rect x="54" y="0" width="3" height="24"/>
        <rect x="40" y="22" width="32" height="5" rx="2"/>
        <ellipse cx="56" cy="52" rx="26" ry="26"/>
        <rect x="0" y="44" width="112" height="12" rx="3"/>
        <circle cx="16" cy="66" r="10"/>
        <circle cx="96" cy="66" r="10"/>
        <circle cx="16" cy="66" r="4" fill="var(--cutout)"/>
        <circle cx="96" cy="66" r="4" fill="var(--cutout)"/>
        <circle cx="56" cy="48" r="9" fill="var(--cutout)"/>
      </svg>
      <h2 class="service-title" style="margin-top:22px;">Business<br>Aircrafts</h2>
    </div>

    <div class="service service-commercial" style="left:591px; top:104px;">
      <svg width="134" height="76" viewBox="0 0 134 76" fill="var(--gold)">
        <rect x="62" y="0" width="10" height="30" rx="4"/>
        <rect x="40" y="14" width="54" height="7" rx="3"/>
        <path d="M0 44 L50 30 H84 L134 44 V52 L84 56 H50 L0 52 Z"/>
        <ellipse cx="67" cy="46" rx="20" ry="16"/>
        <circle cx="33" cy="64" r="10"/>
        <circle cx="101" cy="64" r="10"/>
        <circle cx="33" cy="64" r="4" fill="var(--cutout)"/>
        <circle cx="101" cy="64" r="4" fill="var(--cutout)"/>
        <ellipse cx="67" cy="45" rx="8" ry="5" fill="var(--cutout)"/>
      </svg>
      <h2 class="service-title" style="margin-top:21px;">Commercial<br>Aircrafts</h2>
    </div>

    <div class="service service-amphibious" style="left:810px; top:101px;">
      <svg width="80" height="78" viewBox="0 0 84 80" fill="none" stroke="var(--gold)" stroke-width="4" stroke-linejoin="round">
        <line x1="26" y1="4" x2="58" y2="4"/>
        <line x1="42" y1="4" x2="42" y2="12"/>
        <path d="M42 12 C52 14 54 26 54 40 L80 58 V64 L54 56 L52 68 L62 74 V78 H22 V74 L32 68 L30 56 L4 64 V58 L30 40 C30 26 32 14 42 12 Z"/>
        <ellipse cx="42" cy="40" rx="5" ry="9"/>
      </svg>
      <h2 class="service-title" style="margin-top:22px;">Amphibious<br>Aircrafts</h2>
    </div>

    <div class="service service-operation" style="left:468px; top:309px;">
      <svg width="88" height="60" viewBox="0 0 88 60" fill="var(--gold)">
        <rect x="0" y="6" width="32" height="6" rx="3"/>
        <rect x="0" y="20" width="32" height="6" rx="3"/>
        <rect x="0" y="34" width="32" height="6" rx="3"/>
        <rect x="0" y="48" width="32" height="6" rx="3"/>
        <path d="M40 4 C74 -4 92 18 86 36 C80 56 60 62 40 56 C34 40 34 20 40 4 Z M48 14 C46 26 46 36 48 48 C62 52 74 46 76 32 C78 18 64 10 48 14 Z"/>
      </svg>
      <h2 class="service-title" style="margin-top:25px;">Operation<br>Setup</h2>
    </div>

    <div class="service service-training" style="left:693px; top:289px;">
      <svg width="68" height="88" viewBox="0 0 68 88" fill="var(--gold)">
        <path d="M8 16 C12 2 56 2 60 16 C58 22 54 24 34 24 C14 24 10 22 8 16 Z"/>
        <rect x="16" y="23" width="36" height="5" rx="2"/>
        <path d="M20 28 H48 V38 C48 48 42 54 34 54 C26 54 20 48 20 38 Z"/>
        <rect x="28" y="50" width="12" height="8"/>
        <path d="M2 88 C2 68 14 58 26 56 L34 64 L42 56 C54 58 66 68 66 88 Z"/>
        <path d="M30 62 H38 L36 68 L40 84 L34 88 L28 84 L32 68 Z" fill="var(--cutout)"/>
      </svg>
      <h2 class="service-title" style="margin-top:16px;">Maintenance &amp;<br>Crew Training</h2>
    </div>
  </main>

  <footer class="site-footer">
    <p class="copyright">© 2016 Veltrisk inc. All Rights Reserved</p>
    <div class="social" aria-label="Social links">
      <span></span><span></span><span></span><span></span>
    </div>
  </footer>
</div>
</body>
</html>
```